Skyward Rovers

I would like to re-fresh my existing web page with something more elegant and professional and what will match with my new logo. From the page it should be clearly seen that I organize and sell flying safaris, it should not be tightened only to Africa, should be general.

Page to be re-freshed:
http://skyward-rovers.example

Target Market(s)

Pilots and non-pilots who are going to have a bush flying safari in Africa

Industry/Entity Type

It Professional

```html
<!DOCTYPE html>
<html lang="en">
<head>
<meta charset="utf-8">
<title>Skyward Rovers – Flying Safaris</title>
<link rel="stylesheet" href="https://fonts.googleapis.com/css2?family=Cinzel:wght@400;700&family=Arimo:wght@400;700&display=swap">
<style>
:root{
  --paper:#f6f0dc;
  --paper-dark:#efe4c4;
  --cream:#f5f1e4;
  --ink:#555149;
  --heading-olive:#7a8a14;
  --green:#7b8f18;
  --orange:#d2742c;
  --red:#a1251a;
  --brown:#6e4a22;
  --nav-olive:#8c8a10;
  --nav-orange:#d8782a;
  --nav-red:#b02a1c;
  --nav-brown:#7a4e1a;
  --footer:#262626;
  --footer-text:#d6d6d6;
  --link-green:#a3bf2a;
  --link-orange:#e6822e;
}
*{box-sizing:border-box;margin:0;padding:0}
html,body{width:1062px;height:1200px;overflow:hidden}
body{position:relative;background:var(--cream);font-family:"Arimo",Arial,sans-serif;color:var(--ink)}
.top-band{position:absolute;left:0;top:0;width:1062px;height:546px;
  background:radial-gradient(ellipse at 30% 20%,#f9f3da 0%,var(--paper) 50%,var(--paper-dark) 100%)}
.utility-nav{position:absolute;right:12px;top:15px;font-size:12px;color:#666}
.utility-nav a{color:#555;text-decoration:none}
.utility-nav span{margin:0 12px}
.header-card{position:absolute;left:79px;top:44px;width:903px;height:459px;background:#fff;
  box-shadow:0 6px 14px rgba(0,0,0,.18);border-radius:2px}
.brand{position:absolute;left:18px;top:34px;display:flex;align-items:center;gap:10px}
.brand-dot{width:26px;height:26px;border-radius:50%;background:#3a3633}
.brand-name{font-family:"Cinzel",serif;font-size:28px;font-weight:700;color:#3a3633;letter-spacing:1px}
.main-nav{position:absolute;right:10px;top:50px;font-family:"Cinzel",serif;font-size:15px;display:flex;gap:16px;color:#888}
.main-nav a{text-decoration:none}
.main-nav .tours{color:var(--nav-olive)}
.main-nav .training{color:var(--nav-orange)}
.main-nav .ppl{color:var(--nav-red)}
.main-nav .gallery{color:var(--nav-brown)}
.hero{position:absolute;left:10px;top:106px;width:885px;height:343px;border-radius:3px;overflow:hidden;
  background:linear-gradient(90deg,#8a6a12 0%,#9b7a1e 35%,#c89038 55%,#b88024 72%,#6f7a22 100%)}
.hero-copy{position:absolute;left:49px;top:110px;font-family:"Cinzel",serif;color:#fff;font-size:16px;line-height:26px;letter-spacing:.5px;text-shadow:0 1px 2px rgba(0,0,0,.4)}
.hero-btn{position:absolute;left:49px;top:172px;width:236px;height:42px;border-radius:3px;
  background:linear-gradient(#c8352a,#9a1e15);box-shadow:0 2px 3px rgba(0,0,0,.35);
  display:flex;align-items:center;gap:10px;padding-left:28px;font-family:"Cinzel",serif;font-size:19px;color:#fff}
.hero-dots{position:absolute;left:425px;top:317px;display:flex;gap:16px}
.hero-dots i{width:12px;height:12px;border-radius:50%;background:#3b3b3b;border:2px solid #777}
.hero-dots i.on{background:#fff;border-color:#aaa}
.features{position:absolute;left:79px;top:554px;width:903px;height:268px;background:#ede7d4}
.card{position:absolute;top:15px;width:207px;height:242px;border:1px solid rgba(0,0,0,.2);color:#fff}
.card h2{font-family:"Cinzel",serif;font-size:16px;font-weight:400;margin:9px 0 0 14px;letter-spacing:.5px}
.card .photo{position:absolute;left:10px;top:37px;width:188px;height:129px;border:1px solid rgba(255,255,255,.5)}
.card p{position:absolute;left:21px;top:180px;width:175px;font-size:11.5px;line-height:16.5px}
.card.green{left:14px;background:var(--green)}
.card.orange{left:239px;background:var(--orange)}
.card.red{left:463px;background:var(--red)}
.card.brown{left:688px;background:var(--brown)}
.rule{position:absolute;left:79px;top:833px;width:903px;height:1px;background:#d8d2c0}
.intro{position:absolute;left:79px;top:861px;width:903px}
.intro h1{font-family:"Cinzel",serif;font-size:18px;font-weight:700;color:var(--heading-olive);letter-spacing:.5px}
.intro p{margin-top:14px;font-size:12.5px;line-height:20.3px;color:#5a5650}
.btn-more{display:inline-block;margin-top:12px;padding:8px 14px;background:linear-gradient(#555,#333);color:#fff;font-size:13.5px;border-radius:2px;box-shadow:0 1px 2px rgba(0,0,0,.4)}
.site-footer{position:absolute;left:0;top:1042px;width:1062px;height:158px;background:var(--footer);color:var(--footer-text)}
.col-links{position:absolute;left:81px;top:18px;width:140px;height:124px;border-right:1px solid #444}
.site-footer h3{font-size:13px;font-weight:400;color:#ddd}
.col-links ul,.col-contact ul{list-style:none;margin-top:14px}
.site-footer li{font-size:11.5px;line-height:26px;padding-left:4px}
.col-links li{color:var(--link-green)}
.col-contact{position:absolute;left:270px;top:18px;width:414px;height:124px;border-right:1px solid #444}
.col-contact li{color:var(--link-orange)}
.contact-lines{position:absolute;left:115px;top:32px;font-size:11.5px;color:var(--link-orange);line-height:18.5px}
.contact-lines p{margin-bottom:9px}
.footer-brand{position:absolute;right:0;top:28px;width:270px;display:flex;align-items:center;justify-content:flex-end;gap:10px;padding-right:17px}
.footer-brand .brand-dot{background:#6a6a6a}
.footer-brand .brand-name{color:#6a6a6a;font-size:26px}
.copyright{position:absolute;right:17px;top:111px;text-align:right;font-size:11.5px;line-height:18.5px;color:#bbb}
</style>
</head>
<body>
<div class="top-band"></div>
<nav class="utility-nav"><a href="#">Home</a><span>|</span><a href="#">Contact</a></nav>

<header class="header-card">
  <div class="brand"><span class="brand-dot"></span><span class="brand-name">Skyward Rovers</span></div>
  <nav class="main-nav">
    <a class="tours" href="#">Tours</a><span>|</span>
    <a class="training" href="#">Training</a><span>|</span>
    <a class="ppl" href="#">PPL Validation</a><span>|</span>
    <a class="gallery" href="#">Gallery</a>
  </nav>
  <section class="hero" role="img" aria-label="Close-up of a lion in golden savanna grass with a faded compass">
    <div class="hero-copy">Welcome to the world of adventure<br>...of a lifetime</div>
    <div class="hero-btn">
      <svg width="20" height="20" viewBox="0 0 20 20"><circle cx="10" cy="10" r="9" fill="#eee" stroke="#999"/><path d="M8 5.5 12.5 10 8 14.5" fill="none" stroke="#555" stroke-width="2.2"/></svg>
      Build Your Trip
    </div>
    <div class="hero-dots"><i class="on"></i><i></i><i></i><i></i></div>
  </section>
</header>

<section class="features">
  <article class="card green">
    <h2>Guided Tours</h2>
    <div class="photo" role="img" aria-label="Giraffe beside a safari vehicle in the bush" style="background:linear-gradient(160deg,#9aa070,#7c6a3e 55%,#4c4a2a)"></div>
    <p>For the social pilot who wants to enjoy a luxury safari flying in the bush</p>
  </article>
  <article class="card orange">
    <h2>Self Guided Tours</h2>
    <div class="photo" role="img" aria-label="Open safari vehicle driving through sunlit bush" style="background:linear-gradient(150deg,#e8d9a4,#8a7a3a 45%,#3c3426)"></div>
    <p>For the more adventurous and experienced pilot, wanting to set off on his/her own</p>
  </article>
  <article class="card red">
    <h2>Sample Tours</h2>
    <div class="photo" role="img" aria-label="Aerial view of elephants crossing shallow water" style="background:linear-gradient(170deg,#8fa4c6,#5a7ab0 55%,#c9c6b6)"></div>
    <p>Check our sample tours to give your the feeling of the options</p>
  </article>
  <article class="card brown">
    <h2>Build Your Trip</h2>
    <div class="photo" role="img" aria-label="Bush camp with tents and campfire under a starry night sky" style="background:linear-gradient(180deg,#2c3c6e,#3e4c74 55%,#6a5030 80%,#d88a30)"></div>
    <p>Try to design your own tour so we can review and send an offer accordingly</p>
  </article>
</section>

<div class="rule"></div>

<section class="intro">
  <h1>Welcome to the world of Skyward Rovers</h1>
  <p>Skyward Rovers organises and facilitates self-fly safaris through Southern Africa. What better way to see the wonders of this land than from the pilot's seat of your own aircraft. Whether you're a PPL wanting to experience something beyond flying circuits at your local airfield, a seasoned ATP looking to recapture that passion for flying, or a traveller wanting to experience Africa from a bird's perspective, alone or as part of a group, the flying in this part of the world offers a truly rewarding and unforgettable experience.</p>
  <span class="btn-more">View more</span>
</section>

<footer class="site-footer">
  <div class="col-links">
    <h3>Quick Links</h3>
    <ul><li>• Guided tours</li><li>• Self Guided tours</li><li>• Sample Tours</li><li>• Build your Trip</li></ul>
  </div>
  <div class="col-contact">
    <h3>Quick Contact</h3>
    <ul><li>• Home</li><li>• About Us</li><li>• Gallery</li><li>• Contact Us</li></ul>
    <div class="contact-lines">
      <p>Jonas Berkel - Skyward Rovers<br>Norvane Bank, IBAN CH9300762011623852957</p>
      <p>Call Us : +41 00 555 01 23 &nbsp;&nbsp; | &nbsp;&nbsp; Fax : 555 010 4477</p>
      <p>E-mail : info@skyward-rovers.example</p>
    </div>
  </div>
  <div class="footer-brand"><span class="brand-dot"></span><span class="brand-name">Skyward Rovers</span></div>
  <div class="copyright">Copyright &nbsp;©&nbsp; 2013 &nbsp; www.skyward-rovers.example<br>All rights reserved.</div>
</footer>
</body>
</html>
```